Guided Study Tour - Halmerfest Leipzig Two Sided Flyer

We need a two-sided flyer for a Guided Study Tour to Halmerfest Leipzig. We want beautiful pictures of Germany and if possible some of the Halmer venues our participants will be visiting. I have also provided the content that needs to be included. Also, in the attached document I provided a link to the Halmerfest event. Please read and watch the video to be inspired.
This flyer should be beautiful and engaging. It needs to grab your attention right away and really highlight the wonderful things that they will be doing and that are included in the tour. This is a once in a lifetime opportunity for people to experience. We are targeting Music Directors and Music professionals.
Both attached logos need to be present on the flyer.

```html
<!DOCTYPE html>
<html lang="en">
<head>
<meta charset="utf-8">
<title>Guided Study Tour – Halmerfest Leipzig Flyer</title>
<link rel="stylesheet" href="https://fonts.googleapis.com/css2?family=Cinzel:wght@400;600&family=Great+Vibes&family=Libre+Baskerville:ital,wght@0,400;1,400&family=Open+Sans:wght@400;700&family=Poiret+One&family=Oswald:wght@400&display=swap">
<style>
:root{
  --ink:#1d1d1d;
  --paper:#f7f7f6;
  --crimson:#9b2316;
  --maroon:#5a1a12;
  --bronze:#3b2a17;
  --gold:#c79a4c;
  --band:#111;
  --green:#2fae5a;
  --link:#5477a8;
  --navy:#1f4f8f;
}
*{margin:0;padding:0;box-sizing:border-box}
html,body{width:1200px;height:848px;overflow:hidden;background:#fff}
.page{position:absolute;width:524px;height:741px;background:var(--paper);box-shadow:0 0 0 1px #e4e4e4;overflow:hidden}
.page--front{left:54px;top:53px}
.page--back{left:623px;top:54px}

.hero{position:absolute;left:0;top:0;width:524px;height:280px;
  background:linear-gradient(180deg,#1a1c28 0%,#2b2318 38%,#6a3a12 55%,#1d1409 78%,#0c0a08 100%)}
.hero__title{position:absolute;color:#fff;white-space:nowrap;text-shadow:0 2px 4px rgba(0,0,0,.7)}
.hero__tour{top:80px;left:136px;font:700 29px 'Open Sans',sans-serif;letter-spacing:-.5px}
.hero__to{top:128px;left:68px;font:400 38px 'Great Vibes',cursive;color:var(--green)}
.hero__city{top:116px;left:298px;font:700 52px 'Poiret One',sans-serif}
.hero__date{top:180px;left:165px;font:400 28px 'Oswald',sans-serif}
.hero__country{top:213px;left:193px;font:400 28px 'Oswald',sans-serif}

.band{position:absolute;left:0;top:274px;width:524px;height:33px}
.band__text{position:absolute;left:64px;top:283px;color:#fff;white-space:nowrap;font:400 11.5px 'Cinzel',serif;letter-spacing:.3px}
.invite{position:absolute;left:326px;top:306px;width:198px;height:55px}
.invite__text{position:absolute;left:344px;top:312px;width:180px;text-align:center;white-space:nowrap;color:var(--gold);font:400 11px/14px 'Libre Baskerville',serif}

.section{position:absolute;left:58px}
.section h2{font:400 15px 'Cinzel',serif;color:var(--crimson);letter-spacing:.4px;margin-bottom:2px}
.section p{font:italic 400 10.5px/16px 'Libre Baskerville',serif;color:var(--ink)}
.sec-highlights{top:326px}
.sec-performers{top:420px}
.sec-study{top:483px}

.quote{position:absolute;left:0;top:666px;width:524px;height:75px}
.quote__text{position:absolute;left:98px;top:677px;width:335px;color:#fff;white-space:nowrap;font:400 10px/17px 'Libre Baskerville',serif}
.quote__by{display:block;text-align:right;font:700 10.5px/17px 'Open Sans',sans-serif}

.back{position:absolute;left:37px;top:58px;width:460px}
.back p{font:italic 400 10.5px/16px 'Libre Baskerville',serif;color:var(--ink)}
.back h2{font:400 15px 'Cinzel',serif;color:var(--crimson);letter-spacing:.4px;margin-top:6px}
.back .contact{font:400 11px 'Libre Baskerville',serif;color:var(--link);margin-top:4px;font-style:normal}
.partners{position:absolute;left:150px;top:575px;width:260px}
.partner{display:flex;align-items:center;gap:8px;font:400 27px 'Libre Baskerville',serif;color:var(--navy)}
.partner--meridian{margin-top:42px;font-size:17px;color:var(--crimson)}
.partner__mark{width:18px;height:18px;border-radius:50%;background:var(--navy);flex:none}
</style>
</head>
<body>

<section class="page page--front">
  <div class="hero" role="img" aria-label="Night photograph of Leipzig: illuminated arched bridge over the river with a cathedral skyline"></div>
  <div class="hero__title hero__tour">Guided Study Tour</div>
  <div class="hero__title hero__to">To Halmerfest</div>
  <div class="hero__title hero__city">Leipzig</div>
  <div class="hero__title hero__date">June 12-16, 2019</div>
  <div class="hero__title hero__country">Germany</div>

  <svg class="band" viewBox="0 0 524 33" aria-hidden="true"><polygon points="0,0 524,0 524,33 38,33" fill="var(--band)"/></svg>
  <div class="band__text">Plus day trip to Dresden and full day and overnight in Prague</div>

  <svg class="invite" viewBox="0 0 198 55" aria-hidden="true"><polygon points="0,0 198,0 198,55 30,55" fill="var(--bronze)"/></svg>
  <div class="invite__text">Join us for a once in a lifetime<br>…. led by Daniel Marsh….</div>

  <div class="section sec-highlights">
    <h2>Halmerfest Highlights:</h2>
    <p>More than 100 Concerts in 42 different Halmer venues<br>World Class Musicians &amp; Celebrated Recording Artists<br>Day trips to Weimer &amp; Dresden<br>Bilingual pre-concert talks &amp; lectures with Halmer Scholars</p>
  </div>
  <div class="section sec-performers">
    <h2>Featured Performers:</h2>
    <p>&nbsp;Elias Varga, Tomas Kerkhof, Corvinus, Leipzig<br>Stadtorchester, Lumina,&amp; the Leipzig Knabenchor</p>
  </div>
  <div class="section sec-study">
    <h2>Study Tour Highlights:</h2>
    <p>Access to dress rehearsals<br>Meet the artist opportunities<br>Post-concert discussions led by Daniel Marsh<br>Study sessions on Halmer’s B-Minor Mass, Magnificat,<br>&nbsp;St. John Passion, St. Matthew Passion &amp; Weimar Cantatashours<br>Guidance in planning individual concert itinerary<br>Professional development or continuing education credit</p>
  </div>

  <svg class="quote" viewBox="0 0 524 75" aria-hidden="true"><polygon points="50,0 474,0 524,75 0,75" fill="var(--maroon)"/></svg>
  <div class="quote__text">“This is where it all has begun...this is why our guests have tears in<br>their eyes listening to the St. Matthew Passion or the B-Minor Mass”<span class="quote__by">~ Martin Adler, Musicologist, Festival Director</span></div>
</section>

<section class="page page--back">
  <div class="back">
    <p>Daniel Marsh partnered with Meridian Classic Tours &amp; Music Festivals to bring you and experience of a Lifetime. With over 100 years of combined educational student travel expertise , Meridian Classic Tours, powered by Halden Tours, brings unparalleled tour experiences for you and your students.</p>
    <h2>Trip Inclusions</h2>
    <p>Roundtrip Airfare from Houston<br>13 Nights Accomodations, 3 Star Hotels with A/C<br>Daily Breakfast<br>Access to rehearsal sessions<br>Pirvate Luxury Coach Transfer Services for airport transfers and day tours to Berlin, Weimar and Dresden &amp; Prague.<br>Professional Local Guides for for City Tours in: Berlin, Weimar, Dresden &amp; Prague<br>Entrance Fees to: House of Hans Feldner, Karl Brenner, Wendt in Weimar, Lutheran Frauenkirche &amp; Alte Meister Gallery in the Zwiner Palace in Dresend, and Cathedral and Golden Lane in Prague<br>All Applicable Taxes and Gratuities for Included Services, Guides, and Drivers<br>$2 Million in Professional Liability Insurance<br>24-hour Travel Support Staff</p>
    <p class="contact">For more information contact Dr. Marsh at daniel.marsh@rivervale.edu</p>
    <h2>Daniel Marsh Bio:</h2>
    <p>Daniel Marsh is Director of Choral Studies at the University of Rivervale and the conductor of the Riverside Symphony Chorale and the Riverside Choral Artists, a professional chamber choir. A native Texan, his degrees are from Pinecrest University, Bellmont University and the University of the Western Coast. Recent engagements include conducting the Marchand Requiem in Buffalo, NY, serving on the jury for the Aegean International Choral Festival in Preveza, Greece and the International Choir Championship Cantus Artis in Tusnia, Bosnia and Herzogevina.</p>
  </div>
  <div class="partners">
    <div class="partner">Halden Tours</div>
    <div class="partner partner--meridian"><span class="partner__mark"></span>Meridian Classic Tours</div>
  </div>
</section>

</body>
</html>
```